Real Estate Search Site Re-Design of 2 Pages

Looking for designs to optimize 2 pages of our current site design. Our site allows users to find properties to purchase or rent.

Basically there are 4 panes
1. The top red one where you actually type in what you''re looking for.
2. The map pane that shows the properties
3. The scrollable results pane.
4. Property details pane.

A typical search would go like this:
1. User fills in their search criteria in the top pane in red. Clicks Find Homes
2. Site updates the map with properties plotted that fit the criteria. Site also populates the results pane at the bottom. Site shows the most newest property that fits the search criteria on the right.
3. User will scroll through the results pane or the map and click a property.
4. Site will update the property details pane with information on the selected property.

Search/Results Page
This main page needs a search form area, a results area, an area to display details of a property selected, a map to show results, and an area to display a real estate agent's information. The design must be full-screen to use all the space on the screen. All information should fit on a 1366x768 screen size. Please see sample screen shot.

Property Details Page
This one can be fixed width of 978px. This page needs all the elements that are displayed in the sample PNG file. Ideally, we want to be able to see all important information without scrolling on a 1366x768 screen. The important information in this size are Pictures with controls, address, bedrooms, bathrooms, square feet, square feet of the lot, days on market, agent information, and buttons to request a showing or get more information.

Our Goal:
Our goal is to get create a different way to display the data in an effective way. We want different ways to show the search results, maybe a vertical, scrolling list of property information with pictures. Or even a horizontal scrolling results pane. It must contain:

1. A map of the results
2. A way to scroll through the search results (like we have currently in case someone wants to search/sort bedrooms or square footage)
3. A way to view details of the property
4. A way to display agent information/picture

There's a lot of good design work coming through. Thank you.

Perhaps review some other real estate sales sites for ideas on pane configuration. Example site links:
http://www.brovenly.com/homes/for_sale/?gclid=QmTr8k2-xw7HJd3P9Lq0VnE5ZB (brovenly.com)
http://www.pemoda.com/?sem=1.2.1.5.7.1.0.14&gclid=ZKwp42h-ty8NGRmX5BqeuLcHTD (Pemoda.com)
http://www.quivrent.com/map_search/results/i/ (quivrent.com)

Our goal for the redesign is to display the data in a more effective way. Either with a better flow, more pictures, more information, smoother search process. Please see the updated brief for details. The main idea is to show the data in the most effective way possible.

Project Deadline Extended
Reason: Still looking at different ideas for the search results. We are still open for fresh ideas.

Industry/Entity Type

Real Estate

Font styles to use
Sans Serif

Colors
eb1f27

```html
<!DOCTYPE html>
<html lang="en">
<head>
<meta charset="utf-8">
<title>Redhouse Realty – Search</title>
<link href="https://fonts.googleapis.com/css2?family=Source+Sans+3:wght@400;600&display=swap" rel="stylesheet">
<style>
:root{
  --red:#a60000;
  --red-deep:#990000;
  --orange:#ff8200;
  --btn-orange:#f38a14;
  --btn-green:#7ab51d;
  --row-dark:#3b3b3b;
  --row-light:#545454;
  --panel:rgba(40,40,40,.86);
  --map:#e4dfd5;
  --white:#ffffff;
  --footer:#000000;
  --muted:#8a8a8a;
}
*{box-sizing:border-box;margin:0;padding:0}
html,body{width:1200px;height:817px;overflow:hidden}
body{position:relative;font-family:"Source Sans 3",sans-serif;color:var(--white);background:var(--footer)}
.site-header{position:absolute;left:0;top:0;width:1200px;height:118px;background:var(--red)}
.brand{position:absolute;left:140px;top:30px;display:flex;align-items:center;gap:12px}
.brand-mark{width:44px;height:44px;background:var(--orange)}
.brand-name{font-size:32px;font-weight:400;color:var(--white)}
.lang-select{position:absolute;left:884px;top:16px;width:243px;height:34px;background:var(--white);border-radius:4px;color:#555;font-size:13px;line-height:34px;padding-left:16px}
.lang-select::after{content:"";position:absolute;right:10px;top:14px;border:6px solid transparent;border-top-color:#c00;border-bottom:0}
.main-nav{position:absolute;top:74px;left:766px;display:flex;gap:50px;font-size:20px}
.map-area{position:absolute;left:0;top:118px;width:863px;height:447px;background:linear-gradient(160deg,#e8e3da,#dcd6cb 60%,#d7dfcc)}
.search-panel{position:absolute;left:107px;top:228px;width:676px;height:124px;background:var(--panel);border-radius:4px}
.search-panel .label{position:absolute;font-size:18px}
.field{position:absolute;background:var(--white);border-radius:3px;color:#777;font-size:15px;line-height:30px;padding-left:8px;height:31px}
.field.select::after{content:"";position:absolute;right:9px;top:13px;border:6px solid transparent;border-top-color:#777;border-bottom:0}
.btn{position:absolute;border-radius:3px;color:var(--white);font-size:18px;text-align:center}
.btn-find{left:323px;top:16px;width:132px;height:34px;line-height:34px;background:var(--btn-orange)}
.details-pane{position:absolute;left:863px;top:118px;width:337px;height:447px;background:var(--red)}
.details-address{position:absolute;left:12px;top:0;font-size:17px;line-height:23px}
.details-photo{position:absolute;left:9px;top:55px;width:318px;height:170px;border-radius:5px;background:linear-gradient(180deg,#c06a58 0%,#a85a3c 45%,#4d6a6f 80%,#8fb7c5 100%)}
.details-facts{position:absolute;left:0;top:236px;width:337px;text-align:center;font-size:14px;line-height:23px}
.details-facts .row span{margin:0 8px}
.btn-details{left:37px;top:386px;width:110px;height:36px;line-height:36px;background:var(--btn-green);font-size:17px}
.btn-visit{left:166px;top:386px;width:120px;height:36px;line-height:36px;background:var(--btn-orange);font-size:17px}
.results{position:absolute;left:0;top:565px;width:863px;height:212px;border-collapse:collapse;font-size:14px}
.results th{background:var(--orange);height:35px;font-weight:400;font-size:17px;text-align:left}
.results td{height:36px;border-top:1px solid #888}
.results tbody tr:nth-child(odd){background:var(--row-dark)}
.results tbody tr:nth-child(even){background:var(--row-light)}
.results .c{text-align:center}
.agent-pane{position:absolute;left:863px;top:565px;width:337px;height:212px;background:var(--orange)}
.agent-photo{position:absolute;left:30px;top:48px;width:95px;height:95px;border-radius:50%;background:radial-gradient(circle at 50% 40%,#e9cdb8,#6b4a3a 75%);border:3px solid #f3a040}
.agent-title{position:absolute;left:142px;top:18px;font-size:26px}
.agent-info{position:absolute;left:146px;top:58px;width:130px;text-align:center;font-size:15px;line-height:23px}
.site-footer{position:absolute;left:0;top:777px;width:1200px;height:40px;background:var(--footer);color:var(--muted);font-size:12px}
.site-footer .copy{position:absolute;left:963px;top:14px}
.site-footer .code{position:absolute;left:1174px;top:11px}
</style>
</head>
<body>
<header class="site-header">
  <div class="brand"><span class="brand-mark"></span><span class="brand-name">Redhouse Realty</span></div>
  <div class="lang-select">Select your Language</div>
  <nav class="main-nav"><span>Communities</span><span>Locations</span><span>Contacts</span></nav>
</header>

<div class="map-area" role="img" aria-label="Street map of the search area with property markers"></div>

<form class="search-panel">
  <span class="label" style="left:23px;top:20px">Location</span>
  <div class="field" style="left:104px;top:16px;width:214px">Alhambra</div>
  <div class="btn btn-find">Find Homes</div>
  <span class="label" style="left:25px;top:65px">Type</span>
  <div class="field select" style="left:71px;top:62px;width:165px">Condo/ Town house</div>
  <span class="label" style="left:244px;top:65px">Price</span>
  <div class="field select" style="left:292px;top:62px;width:65px">$500</div>
  <span class="label" style="left:368px;top:66px">To</span>
  <div class="field select" style="left:393px;top:62px;width:65px">$1M</div>
  <span class="label" style="left:464px;top:66px">Beds</span>
  <div class="field select" style="left:510px;top:62px;width:45px">3+</div>
  <span class="label" style="left:566px;top:66px">Baths</span>
  <div class="field select" style="left:615px;top:62px;width:45px">2+</div>
</form>

<aside class="details-pane">
  <div class="details-address">1840 Vista Cresta Avenue<br>Rowland Hights</div>
  <div class="details-photo" role="img" aria-label="Photo of the selected house with pool at sunset"></div>
  <div class="details-facts">
    <div>$ 2,388,000 Listing Price</div>
    <div class="row"><span>3 Beds</span><span>3 Baths</span><span>Built in 2014</span></div>
    <div>3,640 Sq. Ft ($656/Sq. Ft.)</div>
    <div>9,866 Sq. Ft. Lot</div>
    <div>25 Days on Market (#AR1344445)</div>
    <div>Courtesy of Hollins Realty George</div>
  </div>
  <div class="btn btn-details">View Details</div>
  <div class="btn btn-visit">Visit Home</div>
</aside>

<table class="results">
  <colgroup><col style="width:208px"><col style="width:160px"><col style="width:100px"><col style="width:65px"><col style="width:70px"><col style="width:85px"><col style="width:85px"><col></colgroup>
  <thead><tr><th style="padding-left:21px">Address</th><th style="padding-left:14px">City</th><th style="padding-left:15px">Price</th><th class="c">Beds</th><th class="c">Baths</th><th class="c">Sq. Ft.</th><th class="c">$/Sq. Ft.</th><th style="padding-left:11px">Days</th></tr></thead>
  <tbody>
    <tr><td style="padding-left:16px">1840 Vista Cresta Avenue</td><td style="padding-left:15px">Rowland Heights</td><td style="padding-left:15px">$1,200,000</td><td class="c">4</td><td class="c">2.5</td><td class="c">1,814</td><td class="c">$765</td><td style="padding-left:18px">5</td></tr>
    <tr><td style="padding-left:16px">1840 Vista Cresta Avenue</td><td style="padding-left:15px">Rowland Heights</td><td style="padding-left:15px">$1,200,000</td><td class="c">4</td><td class="c">2.5</td><td class="c">1,814</td><td class="c">$765</td><td style="padding-left:18px">5</td></tr>
    <tr><td style="padding-left:16px">1840 Vista Cresta Avenue</td><td style="padding-left:15px">Rowland Heights</td><td style="padding-left:15px">$1,200,000</td><td class="c">4</td><td class="c">2.5</td><td class="c">1,814</td><td class="c">$765</td><td style="padding-left:18px">5</td></tr>
    <tr><td style="padding-left:16px">1840 Vista Cresta Avenue</td><td style="padding-left:15px">Rowland Heights</td><td style="padding-left:15px">$1,200,000</td><td class="c">4</td><td class="c">2.5</td><td class="c">1,814</td><td class="c">$765</td><td style="padding-left:18px">5</td></tr>
    <tr><td style="padding-left:16px">1840 Vista Cresta Avenue</td><td style="padding-left:15px">Rowland Heights</td><td style="padding-left:15px">$1,200,000</td><td class="c">4</td><td class="c">2.5</td><td class="c">1,814</td><td class="c">$765</td><td style="padding-left:18px">5</td></tr>
  </tbody>
</table>

<aside class="agent-pane">
  <div class="agent-photo" role="img" aria-label="Portrait of the buyers agent"></div>
  <div class="agent-title">Buyers Agent</div>
  <div class="agent-info">
    <div>Mara Lindell</div>
    <div>(626) 555 - 0148</div>
    <div>mara@homefind.com</div>
    <div style="margin-top:23px">BRE #04418302</div>
  </div>
</aside>

<footer class="site-footer">
  <span class="copy">© 2014.www.companyname.com</span>
  <span class="code">M1</span>
</footer>
</body>
</html>
```